Meadowlark Hollow Homestead youtube channel

I am looking for a youtube banner graphic that will display on my channel.

Meadowlark Hollow Homestead is a first generation small livestock farm and market garden using permaculture practices, rotational grazing, and regenerative agriculture.

A few youtube graphics that I like which include photo thumbnails are:
https://www.vidtubex.example/@PelbrookMeadow
https://www.vidtubex.example/@RuskinDaleFarm

I am very flexible on the design of the banner graphic, however, I'd like it to match my logo colours. Looking forward to seeing what you all come up with!

```html
<!DOCTYPE html>
<html lang="en">
<head>
<meta charset="utf-8">
<title>Meadowlark Hollow Homestead – channel banner proposal</title>
<link href="https://fonts.googleapis.com/css2?family=Catamaran:wght@500&family=Roboto:wght@400;500;700&family=Cabin:wght@700&display=swap" rel="stylesheet">
<style>
  :root{
    --page:#ffffff;
    --ink:#1a1a1a;
    --accent-red:#c8141c;
    --accent-green:#5a9e1a;
    --channel-bg:#141414;
    --channel-text:#f1f1f1;
    --channel-muted:#aaaaaa;
    --frame-dark:#111111;
    --frame-light:#ffffff;
    --caption:#eadf9e;
  }
  *{box-sizing:border-box;margin:0;padding:0}
  html,body{width:1200px;height:986px;overflow:hidden;background:var(--page)}
  .board{position:relative;width:1200px;height:986px;font-family:"Catamaran",sans-serif;color:var(--ink)}

  .intro{position:absolute;top:64px;left:0;width:1200px;text-align:center;font-size:28px;line-height:34px;font-weight:500}

  .channel-mockup{position:absolute;left:28px;top:319px;width:1140px;height:339px;background:var(--channel-bg);
    box-shadow:0 14px 22px rgba(0,0,0,.45);overflow:hidden;font-family:"Roboto",sans-serif}

  .banner{position:absolute;left:0;top:0;width:1140px;height:189px;overflow:hidden;
    background:linear-gradient(180deg,#c9d8e6 0%,#b6c9d8 35%,#6e9a3c 55%,#4f8a22 100%)}
  .photo-frame{position:absolute;width:190px;height:190px;border:7px solid var(--frame-dark);
    box-shadow:0 0 0 3px var(--frame-light),inset 0 0 0 3px var(--frame-light),4px 6px 8px rgba(0,0,0,.5)}
  .photo-frame .caption{position:absolute;left:0;right:0;bottom:44px;text-align:center;font-family:"Cabin",sans-serif;
    font-weight:700;font-size:17px;line-height:19px;color:var(--caption);
    text-shadow:1px 1px 0 #3a2e10,-1px -1px 0 #3a2e10,1px -1px 0 #3a2e10,-1px 1px 0 #3a2e10}
  .photo-frame .caption.top{bottom:auto;top:22px}
  .frame-tillage{left:120px;top:6px;transform:rotate(-15deg);background:linear-gradient(160deg,#6d7a4a,#8a6a45 60%,#b39a6c)}
  .frame-cover{left:310px;top:8px;transform:rotate(15deg);background:linear-gradient(160deg,#7fae3a,#3f6a1c 60%,#4a3a28)}
  .frame-crops{left:482px;top:2px;transform:rotate(-20deg);background:linear-gradient(160deg,#5a4a3a,#c83a24 50%,#e05a3a)}
  .frame-roots{left:686px;top:6px;transform:rotate(20deg);background:linear-gradient(160deg,#8aa070,#5f7d3c 50%,#f29a1a)}
  .frame-livestock{left:888px;top:4px;transform:rotate(-15deg);background:linear-gradient(160deg,#7c8a58,#b4693a 55%,#8e5a30)}

  .channel-info{position:absolute;left:0;top:189px;width:100%;height:150px}
  .avatar{position:absolute;left:134px;top:15px;width:86px;height:86px;border-radius:50%;background:#222;
    display:flex;align-items:center;justify-content:center;text-align:center;color:var(--accent-green);font-size:10px;font-weight:500;line-height:12px;padding:8px}
  .channel-name{position:absolute;left:236px;top:26px;font-size:16px;color:var(--channel-text)}
  .channel-meta{position:absolute;left:236px;top:49px;font-size:9.5px;color:var(--channel-muted)}
  .channel-meta b{color:var(--channel-text);font-weight:500;margin-right:5px}
  .channel-desc{position:absolute;left:236px;top:71px;font-size:9.5px;color:var(--channel-muted)}
  .channel-desc span{margin-left:14px;font-size:12px}
  .subscribe{position:absolute;left:947px;top:30px;width:63px;height:24px;border-radius:12px;background:#f1f1f1;color:#0f0f0f;
    font-size:9.5px;font-weight:500;display:flex;align-items:center;justify-content:center}
  .tabs{position:absolute;left:0;top:120px;width:100%;height:30px;border-bottom:1px solid #3a3a3a}
  .tab{position:absolute;top:8px;font-size:9.5px;font-weight:700;color:var(--channel-muted);letter-spacing:.3px}
  .tab.active{color:var(--channel-text)}
  .tab-underline{position:absolute;left:133px;bottom:-1px;width:72px;height:2px;background:var(--channel-muted)}
  .search-icon{position:absolute;left:576px;top:7px}

  .note{position:absolute;left:40px;top:826px;width:480px;text-align:center;font-size:28px;line-height:33px;font-weight:500}
  .label-available{position:absolute;left:581px;top:826px;font-size:28px;font-weight:500;color:var(--accent-red)}
  .label-current{position:absolute;left:930px;top:893px;font-size:28px;font-weight:500;color:var(--accent-green)}

  .space-preview{position:absolute;left:745px;top:826px;width:173px;height:120px;background:#000;border-top:2px solid var(--accent-red)}
  .space-preview .safe-strip{position:absolute;left:0;top:68px;width:100%;height:30px;border-top:1px solid var(--accent-red);border-bottom:1px solid var(--accent-red);
    background:linear-gradient(90deg,#5f8a2a,#8a6a45 20%,#6f9a34 38%,#c83a24 55%,#e8901a 72%,#a0643a 88%,#4f8a22)}
  .space-preview .mini-info{position:absolute;left:0;top:98px;width:100%;height:22px;background:#1a1a1a}
  .space-preview .mini-avatar{position:absolute;left:20px;top:5px;width:10px;height:10px;border-radius:50%;background:#333}
  .space-preview .mini-line{position:absolute;height:2px;background:#777}
  .space-preview .mini-button{position:absolute;left:146px;top:5px;width:10px;height:4px;border-radius:2px;background:#eee}
</style>
</head>
<body>
<main class="board">
  <p class="intro">Hi!<br>This arrangement can be further modified, if it does meet your likings.<br>The play with the framing of the images and the text style is as well<br>prone to further adjustments and fine tuning.</p>

  <section class="channel-mockup">
    <div class="banner" role="img" aria-label="Channel banner: green rolling meadow under a blue sky with five tilted farm photo frames">
      <div class="photo-frame frame-tillage" role="img" aria-label="Photo of a red tractor working a field">
        <p class="caption">minimal soil<br>disruption</p>
      </div>
      <div class="photo-frame frame-cover" role="img" aria-label="Photo of young corn plants in covered soil">
        <p class="caption">keeping soil<br>covered</p>
      </div>
      <div class="photo-frame frame-crops" role="img" aria-label="Photo of seedlings in red pots">
        <p class="caption top">diverse<br>crops</p>
      </div>
      <div class="photo-frame frame-roots" role="img" aria-label="Photo of orange marigolds among green plants">
        <p class="caption top">maintain<br>living root</p>
      </div>
      <div class="photo-frame frame-livestock" role="img" aria-label="Photo of a brown cow grazing in a pasture">
        <p class="caption">intergated<br>livestock</p>
      </div>
    </div>

    <div class="channel-info">
      <div class="avatar">Meadowlark Hollow Homestead</div>
      <p class="channel-name">Meadowlark Hollow Homestead</p>
      <p class="channel-meta"><b>@meadowlark_hollow</b> 7 subscribers &nbsp;2 videos</p>
      <p class="channel-desc">Meadowlark Hollow Homestead, a first generation small livestock farm and market ...<span>›</span></p>
      <div class="subscribe">Subscribe</div>
      <nav class="tabs">
        <span class="tab active" style="left:153px">HOME</span>
        <span class="tab" style="left:226px">VIDEOS</span>
        <span class="tab" style="left:305px">PLAYLISTS</span>
        <span class="tab" style="left:400px">CHANNELS</span>
        <span class="tab" style="left:496px">ABOUT</span>
        <svg class="search-icon" width="13" height="13" viewBox="0 0 13 13" aria-hidden="true">
          <circle cx="5.5" cy="5.5" r="4" fill="none" stroke="#aaa" stroke-width="1.2"/>
          <line x1="8.5" y1="8.5" x2="12" y2="12" stroke="#aaa" stroke-width="1.2"/>
        </svg>
        <span class="tab-underline"></span>
      </nav>
    </div>
  </section>

  <p class="note">There is more space available<br>in comparison to the examples<br>that you attached to the brief</p>
  <p class="label-available">available &gt;</p>

  <div class="space-preview" aria-label="Full banner area versus the safe area currently used">
    <div class="safe-strip"></div>
    <div class="mini-info">
      <span class="mini-avatar"></span>
      <span class="mini-line" style="left:36px;top:5px;width:30px"></span>
      <span class="mini-line" style="left:36px;top:10px;width:50px"></span>
      <span class="mini-line" style="left:36px;top:16px;width:70px"></span>
      <span class="mini-button"></span>
    </div>
  </div>
  <p class="label-current">&lt; currently used</p>
</main>
</body>
</html>
```